Book Cover (Front and Rear) for E book called Quiet Mazes

Create book cover front and rear book cover for e book called quiet mazes. Quiet Mazes is a book of 99 puzzles made up of Sudoku, word scrambles, word searches, cross words, mine finder.

Looking for a fairly simple cover similar to the attached 2 designs. Must mention title of book (quiet mazes) as well as making it clear that it is a book of puzzles and my name as the author (Hollis Varga). Rear cover basically same colour as front however just plain.

```html
<!DOCTYPE html>
<html lang="en">
<head>
<meta charset="utf-8">
<title>Quiet Mazes — Cover</title>
<link rel="stylesheet" href="https://fonts.googleapis.com/css2?family=Montserrat:ital,wght@0,300;0,400;0,700;0,800;0,900;1,800&display=swap">
<style>
  :root {
    --cover-green: #66b985;
    --title-yellow: #fdd146;
    --ink-slate: #3f5651;
    --board-dark: #1f3a2c;
    --board-mid: #4e8f66;
    --board-gold: #d9ac35;
    --board-edge: #b38a25;
  }
  html, body {
    margin: 0;
    padding: 0;
    width: 1200px;
    height: 851px;
    overflow: hidden;
    background: var(--cover-green);
  }
  .spread {
    position: relative;
    width: 1200px;
    height: 851px;
    background: var(--cover-green);
    font-family: "Montserrat", sans-serif;
    color: var(--ink-slate);
  }
  .front-title {
    position: absolute;
    left: 150px;
    top: 58px;
    width: 310px;
    text-align: center;
    margin: 0;
    line-height: 1;
  }
  .front-title .title-word-top {
    display: block;
    font-weight: 900;
    font-size: 74px;
    letter-spacing: 1px;
    color: var(--title-yellow);
  }
  .front-title .title-word-bottom {
    display: block;
    margin-top: -8px;
    font-weight: 800;
    font-size: 44px;
    letter-spacing: 1px;
    color: var(--ink-slate);
  }
  .puzzle-board {
    position: absolute;
    left: 31px;
    top: 250px;
    width: 550px;
    height: 362px;
  }
  .puzzle-list {
    position: absolute;
    left: 105px;
    top: 630px;
    width: 400px;
    margin: 0;
    text-align: center;
    font-weight: 400;
    font-size: 20px;
    line-height: 28px;
    color: var(--ink-slate);
  }
  .front-author {
    position: absolute;
    left: 105px;
    top: 780px;
    width: 400px;
    margin: 0;
    text-align: center;
    font-weight: 800;
    font-style: italic;
    font-size: 21px;
    letter-spacing: -0.5px;
    color: var(--ink-slate);
  }
  .back-block {
    position: absolute;
    left: 735px;
    top: 388px;
    width: 325px;
    text-align: right;
  }
  .back-title {
    margin: 0;
    line-height: 1;
    font-weight: 800;
    font-size: 38px;
    letter-spacing: 0.5px;
  }
  .back-title .title-word-top { color: var(--title-yellow); }
  .back-title .title-word-bottom { color: var(--ink-slate); }
  .back-author {
    margin: 2px 0 0;
    font-weight: 800;
    font-style: italic;
    font-size: 21px;
    letter-spacing: -0.5px;
    color: var(--ink-slate);
  }
</style>
</head>
<body>
  <main class="spread">
    <section class="front-cover">
      <h1 class="front-title">
        <span class="title-word-top">QUIET</span>
        <span class="title-word-bottom">MAZES</span>
      </h1>

      <svg class="puzzle-board" viewBox="0 0 550 362" role="img" aria-label="Isometric checkerboard puzzle grid in dark green, light green and gold tiles">
        <defs>
          <linearGradient id="board-top" x1="0" y1="0" x2="0.3" y2="1">
            <stop offset="0" stop-color="var(--board-dark)"/>
            <stop offset="0.45" stop-color="var(--board-mid)"/>
            <stop offset="1" stop-color="var(--board-gold)"/>
          </linearGradient>
        </defs>
        <polygon points="0,172 274,354 274,362 0,180" fill="var(--board-edge)"/>
        <polygon points="548,172 274,354 274,362 548,180" fill="var(--board-edge)"/>
        <polygon points="274,0 548,172 274,354 0,172" fill="url(#board-top)"/>
      </svg>

      <p class="puzzle-list">Word&nbsp; scrambles, Word searches<br>Cross words, Mine finder.<br>Sudoku</p>

      <p class="front-author">Hollis Varga</p>
    </section>

    <section class="back-cover">
      <div class="back-block">
        <h2 class="back-title"><span class="title-word-top">QUIET</span> <span class="title-word-bottom">MAZES</span></h2>
        <p class="back-author">Hollis Varga</p>
      </div>
    </section>
  </main>
</body>
</html>
```